IT Services Postcard

I am looking to update and refresh my existing postcard. I would like to keep all the content it has , but make it more modern and elegant. We are a small boutique IT firm here in Miami, FL in business for 15 years. We support all Brelvanta products. I would like highlight that as well on the postcard- "15 years serving South Florida". I would also like to make the following revisions to the bullet points:Change "Included Email & Virus Protection" to Included Antivirus SoftwareChange "Quorvix Pro Remote Control" to "Secure remote computer access"Add the following bullet point "Included Deskora 480 Backup"You can certainly change the images for the bullet points, and refresh the colors and background as well. I have uploaded a copy of the front and back of my last flyer. I target small to medium size businesses who need a good local IT company they can trust. I look forward to working with you. Thank you.
Target Market(s)
Small Businesses
Industry/Entity Type
It Professional
Colors
Designer to choose colors to be used in the design.
Look and feel

```html
<!DOCTYPE html>
<html lang="en">
<head>
<meta charset="utf-8">
<title>Veltrix Tech – IT Services Postcard</title>
<link href="https://fonts.googleapis.com/css2?family=Open+Sans:wght@400;600;700;800&display=swap" rel="stylesheet">
<style>
  :root {
    --blue: #0a86cf;
    --blue-dark: #066fb0;
    --orange: #f77f0f;
    --ink: #1c1c1c;
    --white: #ffffff;
    --page: #ffffff;
  }
  * { margin: 0; padding: 0; box-sizing: border-box; }
  html, body { width: 926px; height: 1200px; overflow: hidden; background: var(--page); }
  body { font-family: "Open Sans", Arial, sans-serif; color: var(--white); position: relative; }

  .postcard-front { position: absolute; left: 0; top: 0; width: 926px; height: 599px; overflow: hidden; }
  .front-shapes { position: absolute; inset: 0; }

  .brand { position: absolute; color: var(--ink); font-weight: 800; line-height: 1; }
  .brand-name { font-size: 50px; letter-spacing: 1px; }
  .brand-tag { font-size: 20px; letter-spacing: 1px; margin-left: 140px; margin-top: 4px; }
  .brand-front { left: 57px; top: 46px; }
  .brand-back { left: 61px; top: 663px; }

  .hero-photo {
    position: absolute; left: 503px; top: -62px; width: 400px; height: 400px; border-radius: 50%;
    background: radial-gradient(circle at 55% 45%, #8a8f99 0%, #c9b8a4 45%, #e3d8cc 80%);
  }

  .question { position: absolute; left: 61px; top: 182px; font-size: 19px; font-weight: 700; }
  .headline { position: absolute; left: 59px; top: 204px; font-size: 52px; font-weight: 800; letter-spacing: 0.5px; }
  .list-title { position: absolute; left: 61px; top: 272px; font-size: 18px; font-weight: 700; }
  .service-list { position: absolute; list-style: none; font-size: 15px; line-height: 23px; }
  .service-list li::before { content: "✓ "; }
  .list-left { left: 61px; top: 300px; }
  .list-left li:last-child { margin-top: 6px; }
  .list-right { left: 383px; top: 311px; line-height: 22.5px; }
  .other-title { position: absolute; left: 61px; top: 431px; font-size: 18px; font-weight: 700; }
  .other-list { position: absolute; left: 61px; top: 458px; font-size: 15px; line-height: 25px; }
  .other-list span::before { content: "✓ "; }
  .other-list .indent { display: block; padding-left: 100px; }

  .years-badge { position: absolute; left: 719px; top: 323px; width: 112px; height: 112px; border-radius: 50%;
    background: var(--white); border: 4px solid var(--orange); text-align: center; color: var(--blue); font-weight: 800; font-style: italic; }
  .years-badge .num { display: block; font-size: 50px; line-height: 58px; margin-top: 8px; }
  .years-badge .unit { display: block; font-size: 17px; line-height: 16px; }
  .ribbon { position: absolute; left: 675px; top: 426px; width: 200px; height: 38px; border-radius: 10px;
    background: var(--white); color: var(--blue); font-size: 14px; font-weight: 800; font-style: italic;
    text-align: center; line-height: 38px; box-shadow: 0 4px 6px rgba(0,0,0,0.25); }

  .offer { position: absolute; right: 49px; top: 478px; text-align: right; font-size: 23px; line-height: 29px; }
  .offer strong { font-weight: 800; }
  .contact-row { position: absolute; left: 46px; top: 552px; width: 832px; display: flex; align-items: center; font-weight: 700; font-size: 19px; }
  .contact-row .item { display: flex; align-items: center; gap: 6px; margin-right: 16px; }
  .contact-row .phone { margin-left: auto; margin-right: 0; font-size: 39px; font-weight: 700; gap: 10px; }

  .slogan { position: absolute; left: 61px; top: 740px; font-size: 37px; font-weight: 800; color: var(--ink); }
  .slogan .accent { color: var(--blue); }

  .postage { position: absolute; left: 744px; top: 662px; width: 121px; height: 115px; border: 1px solid #333;
    color: var(--ink); font-size: 15px; font-weight: 700; text-align: center; line-height: 19px; padding-top: 20px; }

  .partner-badges { position: absolute; left: 53px; top: 1038px; display: flex; gap: 18px; align-items: center; }
  .partner-badges .badge { height: 48px; border-radius: 4px; }
  .badge-a { width: 100px; background: #d9e6f3; }
  .badge-b { width: 95px; background: #1d63a8; }
  .badge-c { width: 72px; background: #cfdff0; }
  .badge-d { width: 140px; background: #e8e8e8; }

  .contact-card { position: absolute; left: 585px; top: 908px; width: 280px; height: 160px; border-radius: 10px;
    overflow: hidden; background: var(--orange); box-shadow: 0 8px 10px -6px rgba(0,0,0,0.35); }
  .contact-card h2 { background: var(--blue); height: 56px; line-height: 60px; text-align: center; font-size: 23px; font-weight: 700; }
  .contact-card ul { list-style: none; text-align: center; font-size: 16.5px; font-weight: 700; line-height: 26px; padding-top: 12px; }
  .contact-card li { display: flex; justify-content: center; align-items: center; gap: 4px; }
  .icon { flex: none; }
</style>
</head>
<body>

<section class="postcard-front">
  <svg class="front-shapes" width="926" height="599" viewBox="0 0 926 599">
    <path d="M0,92 C170,178 420,176 600,98 L926,70 L926,599 L0,599 Z" fill="#0a86cf"/>
    <path d="M300,171 C430,170 530,140 610,96 L650,92 C560,150 440,182 300,171 Z" fill="#f77f0f"/>
    <path d="M880,58 L926,75 L926,92 L880,70 Z" fill="#f77f0f"/>
    <circle cx="703" cy="138" r="212" fill="none" stroke="#f77f0f" stroke-width="1.5"/>
    <path d="M0,455 C120,520 260,548 420,532 C620,512 760,440 926,418 L926,599 L0,599 Z" fill="#f77f0f"/>
  </svg>

  <div class="hero-photo" role="img" aria-label="Photo of a frustrated businessman gesturing at his laptop in an office"></div>

  <div class="brand brand-front">
    <div class="brand-name">VELTRIX TECH</div>
    <div class="brand-tag">MANAGED SERVICES</div>
  </div>

  <p class="question">Are computer problems frustrating you?</p>
  <h1 class="headline">WE CAN HELP!</h1>
  <p class="list-title">Our low cost monthly IT Service includes:</p>

  <ul class="service-list list-left">
    <li>24/7 Monitoring of Servers</li>
    <li>Proactive Desktop &amp; Server Maintenance</li>
    <li>Unlimited Onsite &amp; Remote Support</li>
    <li>Included Antivirus Software</li>
    <li>Monthly Network health Report</li>
  </ul>
  <ul class="service-list list-right">
    <li>Included Deskora 480 Backup</li>
    <li>Secure remote computer access</li>
    <li>Brelvanta Certified Technicians</li>
    <li>Fast Response Times</li>
    <li>No Long Term Contracts</li>
  </ul>

  <p class="other-title">Other Services Offered:</p>
  <p class="other-list">
    <span>Onsite/Offsite Backup Solutions</span>&nbsp; <span>Deskora 480 Migration</span>
    <span class="indent">Norvale Business Voice Edge Installation</span>
  </p>

  <div class="years-badge"><span class="num">15</span><span class="unit">YEARS</span></div>
  <div class="ribbon">SERVING SOUTH FLORIDA</div>

  <p class="offer">Call today and get<br><strong>2 FREE HOURS</strong> of onsite service</p>

  <div class="contact-row">
    <span class="item">
      <svg class="icon" width="18" height="13" viewBox="0 0 18 13"><rect x="1" y="1" width="16" height="11" fill="none" stroke="#fff" stroke-width="1.5"/><path d="M1,1 L9,7 L17,1" fill="none" stroke="#fff" stroke-width="1.5"/></svg>
      support@veltrixtech.com
    </span>
    <span class="item">
      <svg class="icon" width="16" height="16" viewBox="0 0 16 16"><circle cx="8" cy="8" r="7" fill="none" stroke="#fff" stroke-width="1.5"/><ellipse cx="8" cy="8" rx="3" ry="7" fill="none" stroke="#fff" stroke-width="1.3"/><path d="M1,8 H15" stroke="#fff" stroke-width="1.3"/></svg>
      www.veltrixtech.com
    </span>
    <span class="item phone">
      <svg class="icon" width="36" height="36" viewBox="0 0 36 36"><circle cx="18" cy="18" r="16" fill="none" stroke="#fff" stroke-width="2.5"/><path d="M12,10 L15,9 L17,14 L15,16 C16,19 17,20 20,21 L22,19 L27,21 L26,24 C24,27 18,26 14,22 C10,18 9,12 12,10 Z" fill="#fff"/></svg>
      305-555-0148
    </span>
  </div>
</section>

<section class="postcard-back">
  <div class="brand brand-back">
    <div class="brand-name">VELTRIX TECH</div>
    <div class="brand-tag">MANAGED SERVICES</div>
  </div>
  <p class="slogan"><span class="accent">Relax,</span> we can fix IT!</p>

  <div class="postage">U.S. Postage<br>PAID<br>Permit NO<br>4079</div>

  <div class="partner-badges">
    <span class="badge badge-a"></span>
    <span class="badge badge-b"></span>
    <span class="badge badge-c"></span>
    <span class="badge badge-d"></span>
  </div>

  <div class="contact-card">
    <h2>Contact us TODAY!</h2>
    <ul>
      <li>
        <svg class="icon" width="15" height="15" viewBox="0 0 36 36"><circle cx="18" cy="18" r="16" fill="none" stroke="#fff" stroke-width="3"/><path d="M12,10 L15,9 L17,14 L15,16 C16,19 17,20 20,21 L22,19 L27,21 L26,24 C24,27 18,26 14,22 C10,18 9,12 12,10 Z" fill="#fff"/></svg>
        305-555-0148
      </li>
      <li>
        <svg class="icon" width="16" height="12" viewBox="0 0 18 13"><rect x="1" y="1" width="16" height="11" fill="none" stroke="#fff" stroke-width="1.5"/><path d="M1,1 L9,7 L17,1" fill="none" stroke="#fff" stroke-width="1.5"/></svg>
        support@veltrixtech.com
      </li>
      <li>
        <svg class="icon" width="14" height="14" viewBox="0 0 16 16"><circle cx="8" cy="8" r="7" fill="none" stroke="#fff" stroke-width="1.5"/><ellipse cx="8" cy="8" rx="3" ry="7" fill="none" stroke="#fff" stroke-width="1.3"/><path d="M1,8 H15" stroke="#fff" stroke-width="1.3"/></svg>
        www.veltrixtech.com
      </li>
    </ul>
  </div>
</section>

</body>
</html>
```